"STYLE NIBBLES" courses banner ads

Creation of 6 web banners for google display network and 1 image to be used on FaceBook.

Our website: http://www.vormlab-example.org/
Our facebook: https://www.facebook.com/vormlab/

The banners are meant to attract consumers to click and go to our landing page to find out more about our series of short courses training to be held in 4/5* hotels. The courses to be trained are Colour and Styling, Fabric Care and Leather Care.

Example of the short courses landing page: http://www.vormlab-example.org/special-holiday-season-courses/

Target Market(s)

Females, 25-55 years old, interested in learning fashion styling, fabric care

Industry/Entity Type

Fashion

Font styles to use
Sans Serif

Colors
ec1f27
757575

Requirements
Must have
• Image used should have people and are happy/smiling.
• Some samples of pass banner ads images will be included: see the fabric care and open house samples
• Corporate colours are red, grey and black but addition of complementary colours will be great. Not necessary to use all the three corporate colours at the same time.
• Logos - to be provided (VORML)
• TEXT:
• Style Nibbles
• Short Courses held in hotels in June and July 2017
• Find out more!
Nice to have
• Asian person(s) in the image - please propose the stock image if necessary.
Should not have
• clip art
• fashion runway

```html
<!DOCTYPE html>
<html lang="en">
<head>
<meta charset="utf-8">
<title>Style Nibbles – Short Courses Banners</title>
<link rel="stylesheet" href="https://fonts.googleapis.com/css2?family=Open+Sans:ital,wght@0,400;0,600;0,700;1,700;1,800&display=swap">
<style>
  :root {
    --red: #ec1f27;
    --ink: #231f20;
    --grey: #757575;
    --white: #ffffff;
    --stage: #e4e4e4;
    --frame: #8a8a8a;
  }
  * { margin: 0; padding: 0; box-sizing: border-box; }
  html, body { width: 1200px; height: 1200px; overflow: hidden; }
  body {
    background: var(--stage);
    font-family: "Open Sans", Arial, sans-serif;
    position: relative;
  }
  .banner { position: absolute; background: var(--ink); overflow: hidden; }
  .banner svg.art { position: absolute; left: 0; top: 0; }
  .wordmark {
    position: absolute;
    font-weight: 600; color: var(--ink); letter-spacing: 1px;
    white-space: nowrap;
  }
  .text-frame { position: absolute; border: 1px solid var(--frame); }
  .title {
    position: absolute; transform: translateX(-50%);
    background: var(--ink); color: var(--white);
    font-weight: 600; text-align: center; white-space: nowrap;
    padding: 0 10px;
  }
  .copy {
    position: absolute; text-align: center;
    font-style: italic; font-weight: 800; text-transform: uppercase;
    white-space: nowrap;
  }
  .copy.red { color: var(--red); }
  .copy.white { color: var(--white); font-weight: 700; }

  /* skyscraper */
  .skyscraper { left: 38px; top: 98px; width: 202px; height: 1004px; }
  .skyscraper .wordmark { left: 0; right: 0; top: 30px; text-align: center; font-size: 38px; }
  .skyscraper .text-frame { left: 10px; top: 500px; width: 182px; height: 490px; }
  .skyscraper .title { left: 101px; top: 466px; font-size: 28px; line-height: 36px; }
  .skyscraper .copy { left: 0; right: 0; }
  .skyscraper .short { top: 553px; font-size: 32px; line-height: 43px; }
  .skyscraper .held { top: 645px; font-size: 31px; line-height: 40px; }
  .skyscraper .when { top: 777px; font-size: 31px; line-height: 43px; }
  .cta-button {
    position: absolute; left: 50px; top: 948px; width: 120px; height: 23px;
    background: var(--red); color: var(--white); border-radius: 4px;
    font-size: 13px; display: flex; align-items: center; justify-content: center;
    letter-spacing: -0.3px;
  }

  /* leaderboard */
  .leaderboard { left: 332px; top: 848px; width: 681px; height: 254px; }
  .leaderboard .wordmark { left: 34px; top: 160px; font-size: 40px; }
  .leaderboard .text-frame { left: 358px; top: 43px; width: 294px; height: 187px; }
  .leaderboard .title { left: 505px; top: 28px; font-size: 24px; line-height: 28px; }
  .leaderboard .copy { left: 358px; width: 294px; }
  .leaderboard .short { top: 78px; font-size: 26px; line-height: 32px; }
  .leaderboard .held { top: 109px; font-size: 17px; line-height: 22px; }
  .leaderboard .when { top: 143px; font-size: 26px; line-height: 35px; }
  .cta-link {
    position: absolute; left: 555px; top: 202px;
    color: var(--white); font-size: 12px; letter-spacing: -0.2px;
  }
  .cta-link .chev { color: var(--red); font-weight: 700; margin-left: 3px; }
</style>
</head>
<body>

  <section class="banner skyscraper" aria-label="Style Nibbles skyscraper banner">
    <svg class="art" width="202" height="460" viewBox="0 0 202 460">
      <defs>
        <linearGradient id="skyPhoto" x1="0" y1="0" x2="0" y2="1">
          <stop offset="0" stop-color="#f2f1ee"/>
          <stop offset="0.5" stop-color="#d9cfc4"/>
          <stop offset="1" stop-color="#b9a898"/>
        </linearGradient>
      </defs>
      <path role="img" aria-label="Photo of a smiling young woman with a tape measure in a clothing studio"
            fill="url(#skyPhoto)"
            d="M0 0H202V390L186 404L170 408L176 420L150 424L158 436L128 436L136 448L100 444L106 456L0 452Z"/>
    </svg>
    <div class="wordmark">VORML</div>

    <div class="text-frame"></div>
    <div class="title">STYLE<br>NIBBLES</div>
    <p class="copy red short">Short<br>Courses</p>
    <p class="copy white held">Held<br>in<br>Hotels</p>
    <p class="copy red when">June<br>&amp;<br>July 2017</p>
    <a class="cta-button">Find Out More</a>
  </section>

  <section class="banner leaderboard" aria-label="Style Nibbles wide banner">
    <svg class="art" width="681" height="254" viewBox="0 0 681 254">
      <defs>
        <linearGradient id="widePhoto" x1="0" y1="0" x2="1" y2="0">
          <stop offset="0" stop-color="#e8e6e2"/>
          <stop offset="0.6" stop-color="#d6c9bc"/>
          <stop offset="1" stop-color="#bba693"/>
        </linearGradient>
      </defs>
      <path role="img" aria-label="Photo of a smiling young woman with a tape measure in a clothing studio"
            fill="url(#widePhoto)"
            d="M0 0H322L338 40L330 62L346 74L334 98L350 112L338 140L356 150L340 176L352 192L330 206L338 226L316 240L320 254H0Z"/>
    </svg>
    <div class="wordmark">VORML</div>

    <div class="text-frame"></div>
    <div class="title">STYLE NIBBLES</div>
    <p class="copy red short">Short Courses</p>
    <p class="copy white held">Held in Hotels</p>
    <p class="copy red when">June &amp; July<br>2017</p>
    <a class="cta-link">Find Out More<span class="chev">&gt;&gt;</span></a>
  </section>

</body>
</html>
```